A standard Business and Stock Market Website

We are looking for a well designed and attractive website design which deals on the day to day business activities and stock market performance across the globe.

A good reference website for my proposed website is http://quillharbor.com and http://vkp.com

We are basically featuring the leading stock markets such as Pell marsh stock market and others. The Business name is Quarry lane.
I require very bright colors such as blue, green, black, golden.

Easy nagivating of the website is require and the design should also be responsive on mobile devices.

Designs for three pages. The first design should be for the home page, the second for the Economy/ stockmarkets, Third, business and tech. The home image would also feature stocks, economy, business, tech.

```html
<!DOCTYPE html>
<html lang="en">
<head>
<meta charset="utf-8">
<title>Quarry Lane — Business &amp; Markets</title>
<link rel="stylesheet" href="https://fonts.googleapis.com/css2?family=Oswald:wght@300;400;500;600;700&family=Roboto+Condensed:ital,wght@0,400;0,700;1,700&display=swap">
<style>
:root{
  --blue:#2b86a7;
  --blue-light:#5fb4d2;
  --blue-dark:#1e6580;
  --green:#3b9a5a;
  --gold:#f2c21a;
  --ink:#1d1d1d;
  --text:#555;
  --muted:#8c8c8c;
  --rule:#e6e6e6;
  --topbar:#f1f1f1;
  --footer:#f5f5f5;
  --bottom:#ebebeb;
}
*{box-sizing:border-box;margin:0;padding:0}
html,body{width:1200px;height:2671px;overflow:hidden;background:#fff}
body{position:relative;font-family:"Roboto Condensed",Arial,sans-serif;color:var(--ink)}
.abs{position:absolute}
a{color:inherit;text-decoration:none}

/* top bar */
.topbar{left:0;top:0;width:1200px;height:45px;background:var(--topbar)}
.account{left:100px;top:14px;font-size:13px;display:flex;gap:20px;text-transform:uppercase}
.account span+span{border-left:1px solid #bbb;padding-left:20px}
.search{left:682px;top:8px;width:418px;height:35px;background:#fff;border:1px solid #e0e0e0;font-size:12px;color:#aaa;padding:10px 18px}
.search svg{position:absolute;right:16px;top:11px}

/* header */
.logo{left:100px;top:54px;font-family:Oswald,sans-serif;font-weight:600;font-size:44px;letter-spacing:2px;color:#111}
.ticker{top:52px;text-align:center;font-family:Oswald,sans-serif}
.ticker .sym{font-size:26px;font-weight:400;color:#222;line-height:1}
.ticker .val{font-size:36px;font-weight:600;color:var(--green);line-height:1.1;display:flex;align-items:flex-start;justify-content:center;gap:4px}
.ticker .val sup{font-size:18px;line-height:1.2}
.ticker .val svg{margin-top:14px}

/* nav */
.nav{left:0;top:133px;width:1200px;height:59px;background:var(--blue)}
.nav ul{list-style:none;position:absolute;left:100px;width:1000px;top:18px;display:flex;justify-content:space-between;font-family:Oswald,sans-serif;font-weight:300;font-size:16px;color:#fff;letter-spacing:.3px}

/* trending */
.trendbar{left:0;top:192px;width:1200px;height:64px;background:#f4f4f4;border-bottom:1px solid var(--rule)}
.trend-tag{left:100px;top:206px;width:150px;height:33px;background:var(--green);color:#fff;font-family:Oswald,sans-serif;font-size:16px;letter-spacing:1px;padding:6px 0 0 30px;clip-path:polygon(10px 0,100% 0,100% 100%,0 100%)}
.trend-thumb{left:270px;top:206px;width:104px;height:33px;background:linear-gradient(160deg,#eaf3fa,#7fb3da 55%,#dbe9f5)}
.trend-text{left:399px;top:214px;width:620px;white-space:nowrap;overflow:hidden;font-style:italic;font-weight:700;font-size:15px;color:#222}
.arrow-btn{width:25px;height:25px;border:1px solid #bbb;background:#fff;display:flex;align-items:center;justify-content:center}

/* hero */
.hero{left:100px;top:267px;width:594px;height:399px;background:linear-gradient(180deg,#dfe6ee 0%,#aeb9c6 45%,#5f6e80 100%)}
.hero-caption{left:116px;top:516px;width:320px;height:100px;background:rgba(43,134,167,.88);color:#fff;padding:14px 18px}
.hero-caption h2{font-family:Oswald,sans-serif;font-weight:500;font-size:20px;letter-spacing:.5px;margin-bottom:8px}
.hero-caption p{font-size:12px;line-height:18px;color:#e5f2f7}
.hero-arrows{left:358px;top:620px;display:flex;gap:7px}
.hero-arrows .arrow-btn{background:transparent;border-color:#fff;width:25px;height:24px}
.chart-panel{left:721px;top:267px;width:379px;height:196px;background:#fff;border:1px solid #e3e3e3}
.market{left:721px;top:466px;width:379px;height:200px;background:linear-gradient(135deg,#0d4b55 0%,#1a7d80 45%,#0f3f57 100%)}
.market-tag{left:721px;top:466px;width:71px;height:27px;background:var(--gold);font-family:Oswald,sans-serif;font-weight:500;font-size:14px;color:#222;padding:4px 0 0 12px}

/* feature strip */
.strip-img{top:730px;width:182px;height:130px}
.strip-title{top:876px;width:180px;font-weight:700;font-size:13.5px;line-height:21px;color:#111}
.strip-text{top:922px;width:180px;font-size:12px;line-height:21px;color:var(--text)}

/* section headers */
.sec-head{height:53px;background:var(--blue);border-top:5px solid var(--blue-light);color:#fff;font-family:Oswald,sans-serif;font-weight:500;font-size:23px;letter-spacing:.8px;padding:6px 0 0 16px}
.sec-head::before,.sec-head::after{content:"";position:absolute;bottom:-8px;border-top:8px solid var(--blue-dark)}
.sec-head::before{left:0;border-left:8px solid transparent}
.sec-head::after{right:0;border-right:8px solid transparent}

/* news */
.lead-img{width:313px;height:197px}
.lead-title{width:293px;font-family:Oswald,sans-serif;font-weight:500;font-size:15.5px;line-height:22px;color:#111;letter-spacing:.3px}
.lead-text{width:293px;font-size:12px;line-height:21px;color:var(--text)}
.date{font-size:11.5px;color:var(--muted);display:flex;align-items:center;gap:10px}
.more{font-family:Oswald,sans-serif;font-size:12.5px;color:var(--blue);letter-spacing:.5px}
.rule{height:1px;background:var(--rule)}
.mini-img{width:140px;height:93px}
.mini-title{width:160px;font-weight:700;font-size:12.5px;line-height:21px;color:#111}

/* side stories */
.side-img{left:803px;width:297px;height:146px}
.side-title{left:803px;width:297px;font-family:Oswald,sans-serif;font-weight:500;font-size:15.5px;line-height:21px;letter-spacing:.3px;color:#111}
.side-text{left:803px;width:297px;font-size:12px;line-height:21px;color:var(--text)}

/* footer */
.footer{left:0;top:2332px;width:1200px;height:271px;background:var(--footer)}
.foot-col h4{font-family:Oswald,sans-serif;font-weight:500;font-size:15px;letter-spacing:1px;color:#111;margin-bottom:12px}
.foot-col li{list-style:none;font-size:12.5px;line-height:27.6px;color:#333}
.newsletter p{font-size:12.5px;line-height:19px;color:#333;width:260px}
.news-input{width:242px;height:38px;background:#fff;border:1px solid #ddd;font-size:11px;color:#999;padding:12px 11px;margin-top:14px}
.news-btn{width:91px;height:38px;background:var(--blue);color:#fff;font-family:Oswald,sans-serif;font-weight:500;font-size:14px;letter-spacing:.5px;text-align:center;padding-top:9px;margin-top:14px}
.contact-line{display:flex;align-items:center;gap:10px}
.bottom{left:0;top:2603px;width:1200px;height:68px;background:var(--bottom);font-size:13px;color:#333}
.social{display:flex;gap:16px;align-items:center}
.social span{width:12px;height:12px;border-radius:50%;background:#222;display:block}
</style>
</head>
<body>

<!-- top bar -->
<div class="abs topbar"></div>
<div class="abs account"><span>Login</span><span>Sign up</span></div>
<div class="abs search">Search keyword
  <svg width="12" height="12" viewBox="0 0 12 12"><circle cx="5" cy="5" r="3.8" fill="none" stroke="#999" stroke-width="1.5"/><line x1="8" y1="8" x2="11" y2="11" stroke="#999" stroke-width="1.5"/></svg>
</div>

<!-- header -->
<div class="abs logo">Quarry Lane</div>
<div class="abs ticker" style="left:712px;width:100px">
  <div class="sym">RNPA</div>
  <div class="val"><svg width="18" height="11" viewBox="0 0 18 11"><path d="M0 0H18L9 11Z" fill="var(--green)"/></svg>57<sup>.22</sup></div>
</div>
<div class="abs ticker" style="left:855px;width:120px">
  <div class="sym">GRMP 200</div>
  <div class="val"><svg width="18" height="11" viewBox="0 0 18 11"><path d="M0 0H18L9 11Z" fill="var(--green)"/></svg>23<sup>.70</sup></div>
</div>
<div class="abs ticker" style="left:1010px;width:100px">
  <div class="sym">BRQZG</div>
  <div class="val"><svg width="18" height="11" viewBox="0 0 18 11"><path d="M0 0H18L9 11Z" fill="var(--green)"/></svg>39<sup>.15</sup></div>
</div>

<!-- navigation -->
<nav class="abs nav">
  <ul><li>Home</li><li>World</li><li>U.S.</li><li>Politics</li><li>Economy</li><li>Business</li><li>Tech</li><li>Stock Markets</li><li>Opinion</li><li>Arts</li><li>Life</li><li>Real Estate</li></ul>
</nav>

<!-- trending -->
<div class="abs trendbar"></div>
<div class="abs trend-tag">TRENDING</div>
<div class="abs trend-thumb" role="img" aria-label="Thumbnail of a financial chart"></div>
<div class="abs trend-text">Nam libero tempore, cum soluta nobis est eligendi optio cumque nihil impedit quo minus id quod maxime</div>
<div class="abs arrow-btn" style="left:1045px;top:210px"><svg width="8" height="10" viewBox="0 0 8 10"><path d="M6 1L2 5L6 9" fill="none" stroke="#888" stroke-width="1.5"/></svg></div>
<div class="abs arrow-btn" style="left:1077px;top:210px"><svg width="8" height="10" viewBox="0 0 8 10"><path d="M2 1L6 5L2 9" fill="none" stroke="#888" stroke-width="1.5"/></svg></div>

<!-- hero -->
<div class="abs hero" role="img" aria-label="Businessman in a suit with arms raised between glass office towers"></div>
<div class="abs hero-caption">
  <h2>Occasionally Circumstances ...</h2>
  <p>At vero eos et accusamus et iusto odio dignissimos ducimus qui blanditiis praesentium voluptatum ...</p>
</div>
<div class="abs hero-arrows">
  <div class="arrow-btn"><svg width="8" height="10" viewBox="0 0 8 10"><path d="M6 1L2 5L6 9" fill="none" stroke="#fff" stroke-width="1.5"/></svg></div>
  <div class="arrow-btn"><svg width="8" height="10" viewBox="0 0 8 10"><path d="M2 1L6 5L2 9" fill="none" stroke="#fff" stroke-width="1.5"/></svg></div>
</div>

<div class="abs chart-panel">
  <svg width="379" height="196" viewBox="0 0 379 196">
    <text x="6" y="13" font-size="7.5" font-weight="700" fill="#333" font-family="Roboto Condensed,sans-serif">Harbor Systems</text>
    <g font-size="6.5" fill="#4a7" font-family="Roboto Condensed,sans-serif">
      <rect x="68" y="4" width="14" height="10" fill="#e3efe6"/><text x="71" y="12">1d</text>
      <text x="88" y="12">5d</text><text x="102" y="12">1m</text><text x="117" y="12">3m</text><text x="132" y="12">6m</text><text x="147" y="12">1y</text><text x="160" y="12">5y</text><text x="173" y="12">history</text>
      <rect x="264" y="4" width="24" height="10" fill="#3b9a5a"/><text x="268" y="12" fill="#fff">Line</text>
      <text x="294" y="12">Candle</text><text x="324" y="12">OHLC</text>
    </g>
    <rect x="4" y="26" width="346" height="86" fill="#eef4f9" stroke="#dde6ee"/>
    <g stroke="#e3e9ee" stroke-width="1"><line x1="4" y1="48" x2="350" y2="48"/><line x1="4" y1="70" x2="350" y2="70"/><line x1="4" y1="92" x2="350" y2="92"/></g>
    <path d="M4 70 L18 58 L28 64 L40 50 L52 56 L62 46 L74 60 L86 55 L98 72 L110 66 L122 78 L134 70 L146 62 L158 68 L170 58 L182 62 L194 52 L206 60 L218 56 L230 66 L242 60 L254 70 L266 64 L278 56 L290 62 L302 48 L314 54 L326 44 L338 50 L350 42 L350 112 L4 112Z" fill="#cfe0ee"/>
    <path d="M4 70 L18 58 L28 64 L40 50 L52 56 L62 46 L74 60 L86 55 L98 72 L110 66 L122 78 L134 70 L146 62 L158 68 L170 58 L182 62 L194 52 L206 60 L218 56 L230 66 L242 60 L254 70 L266 64 L278 56 L290 62 L302 48 L314 54 L326 44 L338 50 L350 42" fill="none" stroke="#2b6aa0" stroke-width="1.5"/>
    <g font-size="6" fill="#777" font-family="Roboto Condensed,sans-serif"><text x="356" y="32">19.00</text><text x="356" y="52">18.50</text><text x="356" y="74">18.00</text><text x="356" y="96">17.50</text></g>
    <g font-size="6" fill="#777" font-family="Roboto Condensed,sans-serif"><text x="20" y="122">10am</text><text x="110" y="122">12pm</text><text x="200" y="122">2pm</text><text x="300" y="122">4pm</text></g>
    <rect x="4" y="128" width="346" height="24" fill="#f6f9f6" stroke="#e3e9e3"/>
    <path d="M4 142 Q60 134 120 142 T240 142 T350 140" fill="none" stroke="#3b9a5a" stroke-width="1.2"/>
    <g fill="#9ab0c4">
      <rect x="10" y="176" width="3" height="10"/><rect x="30" y="180" width="3" height="6"/><rect x="50" y="178" width="3" height="8"/><rect x="70" y="181" width="3" height="5"/><rect x="90" y="179" width="3" height="7"/><rect x="110" y="182" width="3" height="4"/><rect x="130" y="180" width="3" height="6"/><rect x="150" y="181" width="3" height="5"/><rect x="170" y="179" width="3" height="7"/><rect x="190" y="182" width="3" height="4"/><rect x="210" y="180" width="3" height="6"/><rect x="230" y="178" width="3" height="8"/><rect x="250" y="181" width="3" height="5"/><rect x="270" y="176" width="3" height="10"/><rect x="290" y="172" width="3" height="14"/><rect x="310" y="168" width="3" height="18"/><rect x="330" y="164" width="3" height="22"/><rect x="345" y="160" width="3" height="26"/>
    </g>
    <line x1="4" y1="186" x2="350" y2="186" stroke="#ccc"/>
  </svg>
</div>
<div class="abs market" role="img" aria-label="Stock ticker board with green and orange price figures"></div>
<div class="abs market-tag">Market</div>

<!-- feature strip -->
<div class="abs strip-img" style="left:100px;background:linear-gradient(135deg,#f4f7fb,#b9d0e6 60%,#e9edf2)" role="img" aria-label="Pen resting on printed financial charts"></div>
<div class="abs strip-img" style="left:306px;background:linear-gradient(135deg,#2a2a2a,#9a9a9a 50%,#3a3a3a)" role="img" aria-label="Glass globe on a desk in black and white"></div>
<div class="abs strip-img" style="left:511px;background:linear-gradient(135deg,#d9d9d9,#f3f3f3 50%,#bdbdbd)" role="img" aria-label="Bankruptcy petition document"></div>
<div class="abs strip-img" style="left:716px;background:linear-gradient(135deg,#c79a7d,#8fa27a 55%,#6f7f5a)" role="img" aria-label="Hands exchanging banknotes"></div>
<div class="abs strip-img" style="left:922px;background:linear-gradient(135deg,#06140a,#1d6b2a 55%,#071b0c)" role="img" aria-label="Green stock chart on a dark screen"></div>

<div class="abs strip-title" style="left:100px">Voluptate velit esse quam nihil molestiae ...</div>
<div class="abs strip-title" style="left:306px">Nam libero tempore, cum soluta nobis est ...</div>
<div class="abs strip-title" style="left:511px">Itaque earum rerum hic tenetur a sapiente ...</div>
<div class="abs strip-title" style="left:716px">Labore et dolore magnam aliquam quaerat ...</div>
<div class="abs strip-title" style="left:922px">Voluptate velit esse quam nihil molestiae ...</div>

<div class="abs strip-text" style="left:100px">Ut enim ad minima veniam, quis nostrum exercitationem ullam corporis suscipit laboriosam, nisi ut aliquid ex ea commodi...</div>
<div class="abs strip-text" style="left:306px">But I must explain to you how all this mistaken idea of denouncing pleasure and praising pain was born and I will give you...</div>
<div class="abs strip-text" style="left:511px">Quis autem vel eum iure reprehenderit qui in ea voluptate velit esse quam nihil molestiae consequatur...</div>
<div class="abs strip-text" style="left:716px">No one rejects, dislikes, or avoids pleasure itself, because it is pleasure, but because those who do not know how to pursue...</div>
<div class="abs strip-text" style="left:922px">But who has any right to find fault with a man who chooses to enjoy a pleasure that has no annoying consequences...</div>

<!-- Latest News -->
<div class="abs sec-head" style="left:100px;top:1063px;width:621px">Latest News</div>
<div class="abs lead-img" style="left:100px;top:1150px;background:linear-gradient(135deg,#6b4a3a,#a5703f 45%,#3a3550)" role="img" aria-label="Speaker at a podium in front of a crowd"></div>
<div class="abs lead-title" style="left:427px;top:1154px">Excepteur sint occaecat cupidatat non proident</div>
<div class="abs lead-text" style="left:427px;top:1203px">sed do eiusmod tempor incididunt ut labore et dolore magna aliqua. Ut enim ad minim veniam, quis nostrud exercitation ullamco ...</div>
<div class="abs date" style="left:427px;top:1286px"><svg width="11" height="11" viewBox="0 0 11 11"><rect x=".5" y="1.5" width="10" height="9" fill="none" stroke="#aaa"/><rect x=".5" y="1.5" width="10" height="3" fill="#aaa"/></svg>Monday, 26 May 2015</div>
<div class="abs more" style="left:427px;top:1314px">Read More &gt;</div>
<div class="abs rule" style="left:100px;top:1373px;width:621px"></div>

<div class="abs mini-img" style="left:100px;top:1397px;background:linear-gradient(135deg,#f1f5fa,#5e8fc5 55%,#dce6f1)" role="img" aria-label="Pen on a pie chart report"></div>
<div class="abs mini-title" style="left:255px;top:1403px">Neque porro quisquam est, qui dolorem...</div>
<div class="abs date" style="left:255px;top:1462px"><svg width="11" height="11" viewBox="0 0 11 11"><rect x=".5" y="1.5" width="10" height="9" fill="none" stroke="#aaa"/><rect x=".5" y="1.5" width="10" height="3" fill="#aaa"/></svg>Monday, 26 May 2015</div>
<div class="abs mini-img" style="left:424px;top:1397px;background:linear-gradient(180deg,#e3a14a,#8a5a2a 60%,#2d2012)" role="img" aria-label="Silhouette jumping at sunset between year numbers"></div>
<div class="abs mini-title" style="left:580px;top:1403px">Duis aute irure dolor in reprehenderit ...</div>
<div class="abs date" style="left:580px;top:1462px"><svg width="11" height="11" viewBox="0 0 11 11"><rect x=".5" y="1.5" width="10" height="9" fill="none" stroke="#aaa"/><rect x=".5" y="1.5" width="10" height="3" fill="#aaa"/></svg>Monday, 26 May 2015</div>

<div class="abs mini-img" style="left:100px;top:1526px;background:linear-gradient(135deg,#2c4d7a,#d6dde6 55%,#3b5d8c)" role="img" aria-label="Glasses resting on folded newspapers"></div>
<div class="abs mini-title" style="left:255px;top:1532px">Similique sunt in culpa qui officia ...</div>
<div class="abs date" style="left:255px;top:1591px"><svg width="11" height="11" viewBox="0 0 11 11"><rect x=".5" y="1.5" width="10" height="9" fill="none" stroke="#aaa"/><rect x=".5" y="1.5" width="10" height="3" fill="#aaa"/></svg>Monday, 26 May 2015</div>
<div class="abs mini-img" style="left:424px;top:1526px;background:linear-gradient(135deg,#e8e8e8,#9a9a9a 55%,#d0d0d0)" role="img" aria-label="Hands typing on a laptop under a magnifier"></div>
<div class="abs mini-title" style="left:580px;top:1532px">Nor again is there anyone who loves ...</div>
<div class="abs date" style="left:580px;top:1591px"><svg width="11" height="11" viewBox="0 0 11 11"><rect x=".5" y="1.5" width="10" height="9" fill="none" stroke="#aaa"/><rect x=".5" y="1.5" width="10" height="3" fill="#aaa"/></svg>Monday, 26 May 2015</div>

<!-- Recent Posts -->
<div class="abs sec-head" style="left:100px;top:1698px;width:621px">Recent Posts</div>
<div class="abs lead-img" style="left:100px;top:1786px;background:linear-gradient(180deg,#6f8a55,#8e9a86 50%,#5d6670)" role="img" aria-label="Runners racing along a city street"></div>
<div class="abs lead-title" style="left:427px;top:1789px">Excepteur sint occaecat cupidatat non proident</div>
<div class="abs lead-text" style="left:427px;top:1838px">sed do eiusmod tempor incididunt ut labore et dolore magna aliqua. Ut enim ad minim veniam, quis nostrud exercitation ullamco ...</div>
<div class="abs date" style="left:427px;top:1921px"><svg width="11" height="11" viewBox="0 0 11 11"><rect x=".5" y="1.5" width="10" height="9" fill="none" stroke="#aaa"/><rect x=".5" y="1.5" width="10" height="3" fill="#aaa"/></svg>Monday, 26 May 2015</div>
<div class="abs more" style="left:427px;top:1949px">Read More &gt;</div>
<div class="abs rule" style="left:100px;top:2005px;width:621px"></div>

<div class="abs mini-img" style="left:100px;top:2030px;background:linear-gradient(135deg,#bdbdbd,#6e6e6e 50%,#c9c9c9)" role="img" aria-label="Small figure standing on a pile of coins"></div>
<div class="abs mini-title" style="left:255px;top:2036px">Similique sunt in culpa qui officia ...</div>
<div class="abs date" style="left:255px;top:2095px"><svg width="11" height="11" viewBox="0 0 11 11"><rect x=".5" y="1.5" width="10" height="9" fill="none" stroke="#aaa"/><rect x=".5" y="1.5" width="10" height="3" fill="#aaa"/></svg>Monday, 26 May 2015</div>
<div class="abs mini-img" style="left:424px;top:2030px;background:linear-gradient(180deg,#dfe3e6,#7d858a 55%,#c8cdd0)" role="img" aria-label="Avenue of bare trees in winter"></div>
<div class="abs mini-title" style="left:580px;top:2036px">Neque porro quisquam est, qui dolorem...</div>
<div class="abs date" style="left:580px;top:2095px"><svg width="11" height="11" viewBox="0 0 11 11"><rect x=".5" y="1.5" width="10" height="9" fill="none" stroke="#aaa"/><rect x=".5" y="1.5" width="10" height="3" fill="#aaa"/></svg>Monday, 26 May 2015</div>

<div class="abs mini-img" style="left:100px;top:2160px;background:linear-gradient(135deg,#1f4f8a,#6fa3d8 55%,#244a7a)" role="img" aria-label="Rising blue bar graph over a city skyline"></div>
<div class="abs mini-title" style="left:255px;top:2166px">Quod maxime placeat facere possimus ...</div>
<div class="abs date" style="left:255px;top:2225px"><svg width="11" height="11" viewBox="0 0 11 11"><rect x=".5" y="1.5" width="10" height="9" fill="none" stroke="#aaa"/><rect x=".5" y="1.5" width="10" height="3" fill="#aaa"/></svg>Monday, 26 May 2015</div>
<div class="abs mini-img" style="left:424px;top:2160px;background:linear-gradient(180deg,#3b5a82,#c9b58a 55%,#24364f)" role="img" aria-label="Silhouettes of people at dusk by the water"></div>
<div class="abs mini-title" style="left:580px;top:2166px">Temporibus autem quibusdam enum sit ...</div>
<div class="abs date" style="left:580px;top:2225px"><svg width="11" height="11" viewBox="0 0 11 11"><rect x=".5" y="1.5" width="10" height="9" fill="none" stroke="#aaa"/><rect x=".5" y="1.5" width="10" height="3" fill="#aaa"/></svg>Monday, 26 May 2015</div>

<!-- Real-Time Stories -->
<div class="abs sec-head" style="left:803px;top:1063px;width:297px">Real-Time Stories</div>

<div class="abs side-img" style="top:1159px;background:linear-gradient(135deg,#c8a98c,#6f5e55 50%,#d9c3a8)" role="img" aria-label="Woman with a coffee cup looking at her phone on a city street"></div>
<div class="abs side-title" style="top:1325px">At vero eos et accusamus et iusto odio dignissimos</div>
<div class="abs side-text" style="top:1368px">To take a trivial example, which of us ever undertakes laborious physical exercise, except to obtain some advantage ...</div>
<div class="abs date" style="left:803px;top:1450px"><svg width="11" height="11" viewBox="0 0 11 11"><rect x=".5" y="1.5" width="10" height="9" fill="none" stroke="#aaa"/><rect x=".5" y="1.5" width="10" height="3" fill="#aaa"/></svg>Monday, 26 May 2015</div>
<div class="abs rule" style="left:803px;top:1490px;width:297px"></div>

<div class="abs side-img" style="top:1519px;background:linear-gradient(135deg,#0d3f73,#3f8cd0 50%,#0b2f57)" role="img" aria-label="Blue financial graph overlaid on office towers"></div>
<div class="abs side-title" style="top:1685px">Sed quia non numquam eius modi tempora incidunt ...</div>
<div class="abs side-text" style="top:1728px">To take a trivial example, which of us ever undertakes laborious physical exercise, except to obtain some advantage ...</div>
<div class="abs date" style="left:803px;top:1810px"><svg width="11" height="11" viewBox="0 0 11 11"><rect x=".5" y="1.5" width="10" height="9" fill="none" stroke="#aaa"/><rect x=".5" y="1.5" width="10" height="3" fill="#aaa"/></svg>Monday, 26 May 2015</div>
<div class="abs rule" style="left:803px;top:1850px;width:297px"></div>

<div class="abs side-img" style="top:1877px;background:linear-gradient(135deg,#5a3b2a,#c79461 50%,#4a3226)" role="img" aria-label="Group of friends laughing over a phone in a café"></div>
<div class="abs side-title" style="top:2043px">Similique sunt in culpa qui officia deserunt mollitia ...</div>
<div class="abs side-text" style="top:2086px">To take a trivial example, which of us ever undertakes laborious physical exercise, except to obtain some advantage ...</div>
<div class="abs date" style="left:803px;top:2170px"><svg width="11" height="11" viewBox="0 0 11 11"><rect x=".5" y="1.5" width="10" height="9" fill="none" stroke="#aaa"/><rect x=".5" y="1.5" width="10" height="3" fill="#aaa"/></svg>Monday, 26 May 2015</div>
<div class="abs rule" style="left:803px;top:2232px;width:297px"></div>

<!-- footer -->
<footer class="abs footer"></footer>
<div class="abs foot-col" style="left:100px;top:2372px">
  <h4>LINKS</h4>
  <ul><li>Team</li><li>Schedule</li><li>News</li><li>Videos</li><li>Photos</li><li>Others</li></ul>
</div>
<div class="abs foot-col newsletter" style="left:253px;top:2372px">
  <h4>JOIN OUR NEWSLETTER</h4>
  <p>Excepteur sint occaecat cupidatat non proident, sunt in culpa qui</p>
  <div class="news-input">Enter Your Email</div>
  <div class="news-btn">SUBSCRIBE</div>
</div>
<div class="abs foot-col" style="left:589px;top:2372px">
  <h4>INFORMATION</h4>
  <ul><li>Terms &amp; Conditions</li><li>Privacy policy</li><li>Disclaimer</li><li>Contact us</li><li>Sitemap</li></ul>
</div>
<div class="abs foot-col" style="left:787px;top:2372px">
  <h4>WHY US</h4>
  <ul><li>Customers</li><li>Team</li><li>FAQ</li><li>News</li><li>Others</li></ul>
</div>
<div class="abs foot-col" style="left:954px;top:2372px">
  <h4>CONTACT INFO</h4>
  <ul>
    <li style="font-family:Oswald,sans-serif;font-weight:500;font-size:13.5px;color:#111">Quarry Lane</li>
    <li style="line-height:24px">No Street Address,<br>State Code, Country</li>
    <li class="contact-line"><svg width="11" height="11" viewBox="0 0 12 12"><path d="M2 1L4.5 1L5.5 4L4 5Q5 7.5 7 8L8 6.5L11 7.5L11 10Q10 11.5 8 11Q2 9 1 3Q1 1.5 2 1Z" fill="#333"/></svg>+11 (0) 482 915 30</li>
    <li class="contact-line"><svg width="12" height="9" viewBox="0 0 12 9"><rect width="12" height="9" fill="#333"/><path d="M0 0L6 5L12 0" fill="none" stroke="#f5f5f5" stroke-width="1"/></svg>hello@quarrylane.com</li>
  </ul>
</div>

<div class="abs bottom"></div>
<div class="abs" style="left:100px;top:2627px;font-size:13px;color:#333">© 2016. QUARRY LANE. All rights reserved</div>
<div class="abs" style="left:777px;top:2627px;font-size:13px;color:#333">Connect with our social network :</div>
<div class="abs social" style="left:952px;top:2631px"><span></span><span></span><span></span><span></span><span></span></div>

</body>
</html>
```